Everything fresh, everything new

When I take over the practice, I would like to breathe new life into the practice. I want a business card design that catches the eye and brings a breath of fresh air

```html
<!DOCTYPE html>
<html lang="de">
<head>
<meta charset="utf-8">
<title>Physioquell – Visitenkarte</title>
<link href="https://fonts.googleapis.com/css2?family=Montserrat:wght@700&family=Open+Sans:wght@400;600&display=swap" rel="stylesheet">
<style>
  :root {
    --stage: #1b1b1c;
    --card-white: #ffffff;
    --brand-green: #8bc440;
    --brand-dark: #4b4b4d;
    --ink: #3f3f41;
    --on-dark: #ffffff;
  }
  * { box-sizing: border-box; margin: 0; padding: 0; }
  html, body {
    width: 1200px; height: 875px; overflow: hidden;
    background: var(--stage);
    font-family: "Open Sans", sans-serif;
  }
  .canvas {
    position: relative; width: 1200px; height: 875px;
    display: flex; align-items: center; justify-content: center; gap: 40px;
  }
  .card {
    position: relative; width: 540px; height: 310px;
    border-radius: 18px; overflow: hidden;
    box-shadow: 0 18px 40px rgba(0,0,0,.45);
  }
  /* front */
  .card--front {
    background: var(--card-white);
    display: flex; align-items: center; justify-content: center;
  }
  .brand { display: flex; align-items: center; gap: 14px; }
  .brand__dot {
    width: 22px; height: 22px; border-radius: 50%;
    background: var(--brand-green);
  }
  .brand__name {
    font-weight: 600; font-size: 50px; letter-spacing: -0.5px;
    color: var(--ink); line-height: 1;
  }
  .brand__tagline {
    margin-top: 8px; text-align: right;
    font-size: 13px; color: var(--ink); letter-spacing: .3px;
  }
  /* back */
  .card--back { background: var(--brand-dark); }
  .card__band { position: absolute; inset: 0; }
  .back__brand {
    position: absolute; left: 34px; top: 58px;
    font-weight: 600; font-size: 36px; color: var(--on-dark);
    letter-spacing: -0.3px; line-height: 1;
  }
  .contact {
    position: absolute; left: 34px; bottom: 30px;
    list-style: none; color: var(--on-dark);
    font-size: 13px; line-height: 19px;
  }
  .contact__item { display: flex; align-items: flex-start; gap: 10px; }
  .contact__icon { width: 12px; height: 12px; margin-top: 3px; flex: none; fill: var(--on-dark); }
  .person {
    position: absolute; right: 22px; top: 132px; text-align: right;
    color: var(--on-dark);
  }
  .person__name {
    font-family: "Montserrat", sans-serif; font-weight: 700;
    font-size: 18px; letter-spacing: .3px; text-transform: uppercase;
  }
  .person__role { font-size: 13px; margin-top: 2px; }
</style>
</head>
<body>
<main class="canvas">
  <section class="card card--front" aria-label="Vorderseite">
    <div>
      <div class="brand">
        <span class="brand__dot"></span>
        <span class="brand__name">Physioquell</span>
      </div>
      <p class="brand__tagline">Kraft für jeden Tag</p>
    </div>
  </section>

  <section class="card card--back" aria-label="Rückseite">
    <svg class="card__band" viewBox="0 0 540 310" preserveAspectRatio="none" aria-hidden="true">
      <path d="M0 0 H320 C385 0 395 80 375 150 C360 215 360 270 395 310 H0 Z" fill="var(--brand-green)"/>
    </svg>
    <p class="back__brand">Physioquell</p>
    <ul class="contact">
      <li class="contact__item">
        <svg class="contact__icon" viewBox="0 0 12 12"><path d="M6 0a4 4 0 0 0-4 4c0 3 4 8 4 8s4-5 4-8a4 4 0 0 0-4-4zm0 5.5A1.5 1.5 0 1 1 6 2.5a1.5 1.5 0 0 1 0 3z"/></svg>
        <span>Your Address, City<br>State, Country, Zip 1235</span>
      </li>
      <li class="contact__item">
        <svg class="contact__icon" viewBox="0 0 12 12"><path d="M2.5 0.5l2 2.2-1 1.3a7 7 0 0 0 4.5 4.5l1.3-1 2.2 2-1.2 1.8C5 11 1 7 0.7 1.7z"/></svg>
        <span>(123) 456-7890</span>
      </li>
      <li class="contact__item">
        <svg class="contact__icon" viewBox="0 0 12 12"><path d="M3 0h6a1 1 0 0 1 1 1v10a1 1 0 0 1-1 1H3a1 1 0 0 1-1-1V1a1 1 0 0 1 1-1zm0.5 1.5v8h5v-8z"/></svg>
        <span>(231) 456-7890</span>
      </li>
      <li class="contact__item">
        <svg class="contact__icon" viewBox="0 0 12 12"><path d="M0 2h12v1L6 7 0 3zM0 4.3l6 4 6-4V10H0z"/></svg>
        <span>info@physioquell.de</span>
      </li>
      <li class="contact__item">
        <svg class="contact__icon" viewBox="0 0 12 12"><circle cx="6" cy="6" r="5.2" fill="none" stroke="#fff" stroke-width="1.4"/><path d="M1 6h10M6 1c-2.5 3-2.5 7 0 10M6 1c2.5 3 2.5 7 0 10" fill="none" stroke="#fff" stroke-width="1"/></svg>
        <span>physioquell.de</span>
      </li>
    </ul>
    <div class="person">
      <p class="person__name">Jonas Keller</p>
      <p class="person__role">Founder &amp; CEO</p>
    </div>
  </section>
</main>
</body>
</html>
```